Need a Professional Music artist Website for Doranetunes.com(FOR PHONE AND COMPUTER)

Please supply me with a mock of doranetunes.com.
I need a logo that says Doranet with a lifeline.
I want this to have the navigation bar on top with these pages: About, Booking, Store, Contact, Subscribe, Fan Photos, Pictures, Blog, Events, Videos, faq, become a member, picture, forum and Press.
All the social media icons found on my current website.
I am very much into the look of Margotwenn.com, pixiedorn.com, http://www.velbeauty-example.com/index.tmpl and Corwynhalesongs.com
Make it look feminine yet professional. Thank you.

Target Market(s)

Woman from age 13-25.

Industry/Entity Type

Computer

Font styles to use
Script
Other font styles liked:
• warm and sure on typequill-example.com

Colors
757575
1b1b1b
000000
ebdaeb
f8d9e8
f59195
ec1f27
f04a50
f59296

Requirements
Must have
• Lifeline registration with chirpnet account and facetome login , What kind of lifeline are you quiz? , navi mentioned above, store selling page, ask doranet(Tell us your story), About Doranet, Subscribe, Instant play Doranet cam, Advertise here section, Forum, Lifelinescope, Poll, Live chatroom, Show us your best mwah and win a 100 dollar Lumelle giftcard. Professional feel and nice colorful mood.
Nice to have
• How my picture is set up;
2 box most recent blog posts
Lifelines(fans photos slideshow)
2 box vidstream videos
Doranet cam:
My vlog for my fans.
sidebar to the left for advertisement add,
join the lifeliners, and poll to where doranet should be playing next.

```html
<!DOCTYPE html>
<html lang="en">
<head>
<meta charset="utf-8">
<title>Doranet</title>
<link rel="stylesheet" href="https://fonts.googleapis.com/css2?family=Open+Sans:ital,wght@0,300;0,400;0,600;0,700;1,400&display=swap">
<style>
  :root {
    --ink: #000000;
    --night: #050505;
    --paper: #f2f2f2;
    --coral: #f04a50;
    --white: #ffffff;
    --muted: #c8c8c8;
    --arrow: #4a4a4a;
    --facetome: #5a83c0;
    --facetome-dark: #3d63a0;
    --chirpnet: #26b0e3;
    --chirpnet-dark: #1590c2;
    --grey: #757575;
  }
  * { box-sizing: border-box; margin: 0; padding: 0; }
  html, body { width: 1200px; height: 1200px; overflow: hidden; }
  body {
    position: relative;
    background: var(--paper);
    font-family: "Open Sans", Arial, sans-serif;
    color: var(--ink);
  }
  .masthead {
    position: absolute; left: 0; top: 0;
    width: 1200px; height: 466px;
    background: var(--night);
  }
  .brand {
    position: absolute; left: 194px; top: 62px;
    font-size: 46px; font-weight: 300; color: var(--white);
    line-height: 1;
  }
  .bio {
    position: absolute; left: 194px; top: 171px; width: 420px;
    font-size: 10.6px; font-weight: 300; line-height: 14.4px; color: var(--muted);
    white-space: nowrap;
  }
  .gem { position: absolute; left: 374px; top: 264px; }
  .portrait {
    position: absolute; left: 606px; top: 54px;
    width: 258px; height: 412px;
    background: radial-gradient(ellipse at 50% 40%, #8a8a8a 0%, #4a4a4a 45%, #151515 80%, var(--night) 100%);
    border-radius: 120px 120px 0 0;
  }
  .slide-arrow { position: absolute; top: 188px; }
  .slide-arrow.prev { left: 18px; }
  .slide-arrow.next { left: 1126px; }
  .main-nav {
    position: absolute; right: 184px; top: 116px;
    list-style: none; text-align: right;
  }
  .main-nav li {
    font-size: 12px; line-height: 18px; color: var(--white);
    text-transform: uppercase;
  }
  .social {
    position: absolute; left: 1040px; top: 36px;
    list-style: none;
  }
  .social li {
    width: 41px; height: 41px; margin-bottom: 9.3px;
    border-radius: 50%; background: var(--coral);
    color: var(--white); font-size: 7px; font-weight: 600;
    display: flex; align-items: center; justify-content: center;
  }
  .post {
    position: absolute; top: 314px;
    width: 177px; height: 257px;
    background: var(--coral);
    padding: 10px 8px 0 12px;
    white-space: nowrap;
  }
  .post.first { left: 194px; }
  .post.second { left: 412px; padding-left: 14px; }
  .post h2 {
    font-size: 11.6px; font-weight: 700; line-height: 14.4px;
    text-transform: uppercase; margin-bottom: 14px;
  }
  .post p { font-size: 11px; line-height: 14.4px; }
  .signin {
    position: absolute; top: 509px;
    width: 160px; height: 26px; border-radius: 3px;
    display: flex; align-items: center;
    color: var(--white); font-size: 10.5px;
  }
  .signin .mark {
    width: 26px; height: 26px; border-radius: 3px 0 0 3px;
    margin-right: 14px; flex: none;
  }
  .signin.facetome { left: 667px; background: linear-gradient(var(--facetome), var(--facetome-dark)); }
  .signin.facetome .mark { background: var(--facetome-dark); }
  .signin.chirpnet { left: 871px; background: linear-gradient(var(--chirpnet), var(--chirpnet-dark)); }
  .signin.chirpnet .mark { background: var(--chirpnet-dark); }
  .or {
    position: absolute; left: 842px; top: 514px;
    font-size: 10px; font-style: italic; color: var(--grey);
  }
  .feature-links {
    position: absolute; left: 341px; top: 638px;
    list-style: none;
  }
  .feature-links li { font-size: 14.4px; line-height: 17px; text-transform: uppercase; }
</style>
</head>
<body>
  <header class="masthead">
    <div class="brand">Doranet</div>
    <p class="bio">Liora Doranet was born and raised in Staten Island, NY, singing as her<br>primary form of communication as she was plagued with a stutter since<br>birth. As if this hodgepodge flow of speech wasn't enough, at six Liora<br>was diagnosed with dyslexia, a speech impediment, and an ambidextrous<br>ability.</p>
    <svg class="gem" width="40" height="32" viewBox="0 0 40 32" aria-hidden="true">
      <g fill="none" stroke="#ffffff" stroke-width="1.3" stroke-linejoin="round">
        <polygon points="9,2 31,2 38,11 20,30 2,11"/>
        <line x1="2" y1="11" x2="38" y2="11"/>
        <polyline points="9,2 14,11 20,30 26,11 31,2"/>
        <polyline points="14,11 20,2 26,11"/>
      </g>
    </svg>
    <div class="portrait" role="img" aria-label="Black and white portrait of the singer smiling, arms folded, in a sequined dress"></div>
    <svg class="slide-arrow prev" width="38" height="70" viewBox="0 0 38 70" aria-hidden="true">
      <polyline points="36,1 2,35 36,69" fill="none" stroke="var(--arrow)" stroke-width="2"/>
    </svg>
    <svg class="slide-arrow next" width="38" height="70" viewBox="0 0 38 70" aria-hidden="true">
      <polyline points="2,1 36,35 2,69" fill="none" stroke="var(--arrow)" stroke-width="2"/>
    </svg>
    <ul class="main-nav">
      <li>About</li>
      <li>Booking Store</li>
      <li>Contact</li>
      <li>Subscribe</li>
      <li>Fan Photos</li>
      <li>Pictures</li>
      <li>Blog</li>
      <li>Events</li>
      <li>Videos</li>
      <li>FAQ</li>
      <li>Become a Member</li>
      <li>Picture</li>
      <li>Forum</li>
      <li>Press</li>
    </ul>
    <ul class="social">
      <li>facetome</li>
      <li>chirpnet</li>
      <li>photoly</li>
      <li>vidstream</li>
      <li>wavecove</li>
      <li>starbeat</li>
      <li>blogsy</li>
      <li>orchard</li>
    </ul>
  </header>

  <article class="post first">
    <h2>Spring is coming —<br>exclusive interview</h2>
    <p>Hey Lifelines! &nbsp; Mark your<br>calendars for April 15, as<br>an interview focusing on<br>me and my life will be<br>coming out, in addition to a<br>sneak peak of another new<br>track I've been working on,<br>"Thief". Speaking of new<br>tracks, I'm currently record-<br>ing a new song I just wrote,<br>"80's" and I'm going to […]</p>
  </article>
  <article class="post second">
    <h2>New music video<br>"Goodbye" &amp; sneak<br>peek of "Thief"</h2>
    <p>Are you excited? Cause you<br>have no reason not to, as I<br>am absolutely pumped to<br>announce that my new<br>music video "Goodbye" is<br>debuting this Saturday,<br>March 15th at midnight!<br>Goodbye is my answer to<br>the standard-issue break-<br>up song, dedicated to<br>everyone who has ever<br>had to kiss a swamp's […]</p>
  </article>

  <div class="signin facetome"><span class="mark"></span>sign in with facetome</div>
  <span class="or">or</span>
  <div class="signin chirpnet"><span class="mark"></span>sign in with chirpnet</div>

  <ul class="feature-links">
    <li>What kind of lifeline are you quiz?</li>
    <li>Ask Doranet</li>
  </ul>
</body>
</html>
```